New Artwork/Design for Established Weight Loss Podcast

Hello,
I would like new artwork/design for my podcast. It's called True Path Slim Down and has been a consistently top 50 show in the fitness/nutrition category on Orchard. My current design was originally created when I started the podcast over 2 years ago. It's time to refresh and update things! I would like a new design that incorporates a photo of me, but could also be used as a standalone logo for the podcast without my photo. A nice, clean, professional, yet fun design. Here is a Google drive link with professional photos that could be used:
https://files.boxvault.example/folders/8Kqmt47n-x2pLdWeRvaHsTnY6UiOb3Jc?share=1

Here's a little more about the show . There are three big taglines. These do NOT need to be included on the design. I just include them here to help with the feel/theme of the design.

1: To change your body, you must first change your brain.
2: There's so much more to you than just a number (what you weigh).
3: Losing weight is really about gaining life and living the life you've always wanted.

This podcast is all about busy moms, dads, husbands, wives who are working, raising kids, and trying to juggle everything life’s throwing at them … but also want to be the best they can for their family and friends and loved ones.

The podcast is NOT about how to get six-pack abs or how to drop as much weight as possible in 8 weeks. It's about finding sustainable success with your body, peace of mind with food, and improving your relationship with yourself.

Week by week, I provide bite-sized guidance - 20-25 minute episodes that pull back the curtain and reveal the truth about what it takes to lose weight and gain life - what strategy and approach real people are using to get results while escaping the soul-sucking, all-or-nothing diet mentality.

Here's a link to the current artwork: https://files.boxvault.example/file/5Tnh2Gq9bmzrWkxPd-ve-Lo4MJ-e-QBD/view?share=1

And the logo without my photo: https://files.boxvault.example/file/7Hb2Nx4wVcPs_9r63mKqJdzTa1RfEpnpk/view?share=1

I'm open to any colors, but something that either matches the colors of my website or signature "Move Bright Trim Down" program would probably be a smart idea. Here are links to my website and the MBTD logo . . .

Website: https://danewardmentoring.example/

MBTD logo:
https://files.boxvault.example/file/3PQvn8Kd_Rt5Ywmc3xoLeH_9vOPzs2hj/view?share=1

Happy to answer any questions you might have. Thanks.

Target Market(s)

35 to 55 years old, roughly 70% female, 30% male, professionals, primarily in the U.S. and Canada

Industry/Entity Type

nutrition, health, weight loss

Requirements
Must have
• One version with my photo and the same design without my photo
Nice to have
• Open to any colors, but possibly incorporate colors from either my website or MBTD logo (see project description for more info)
Should not have
• Any hardcore fitness or bodybuilding imagery

```html
<!DOCTYPE html>
<html lang="en">
<head>
<meta charset="utf-8">
<title>True Path Slim Down Podcast – Cover Artwork</title>
<link href="https://fonts.googleapis.com/css2?family=Jost:ital,wght@0,300;0,400;1,400&family=Allura&display=swap" rel="stylesheet">
<style>
  :root {
    --canvas: #dcdcdc;
    --paper: #ffffff;
    --charcoal: #3e3e40;
    --teal: #64aea8;
    --ink-light: #ffffff;
    --shadow: rgba(0, 0, 0, 0.35);
  }
  * { box-sizing: border-box; margin: 0; padding: 0; }
  html, body {
    width: 1200px;
    height: 618px;
    overflow: hidden;
    background: var(--canvas);
  }
  .stage {
    position: relative;
    width: 1200px;
    height: 618px;
  }
  .cover {
    position: absolute;
    top: 37px;
    width: 553px;
    height: 553px;
    background: var(--charcoal);
    box-shadow: 2px 3px 6px var(--shadow);
    overflow: hidden;
    font-family: "Jost", "Helvetica Neue", Arial, sans-serif;
  }
  .cover--logo { left: 37px; --cx: 277px; }
  .cover--host { left: 610px; --cx: 172px; }
  .cover__top-band {
    position: absolute;
    left: 0; top: 0;
    width: 100%;
    height: 182px;
    background: var(--paper);
  }
  .cover__line {
    position: absolute;
    left: var(--cx);
    transform: translateX(-50%);
    white-space: nowrap;
    line-height: 1;
  }
  .title-accent {
    font-size: 83px;
    font-style: italic;
    font-weight: 400;
    color: var(--teal);
  }
  .title-accent--one { top: 15px; }
  .title-accent--two { top: 89px; }
  .title-main {
    font-size: 80px;
    font-weight: 300;
    color: var(--ink-light);
  }
  .title-main--one { top: 166px; }
  .title-main--two { top: 238px; }
  .label-podcast {
    top: 337px;
    font-size: 21px;
    font-weight: 400;
    letter-spacing: 0.38em;
    margin-left: 0.19em;
    color: var(--teal);
  }
  .label-with {
    top: 366px;
    font-family: "Allura", cursive;
    font-size: 44px;
    color: var(--ink-light);
  }
  .host-name {
    top: 418px;
    font-size: 36px;
    font-weight: 400;
    color: var(--ink-light);
    letter-spacing: -0.01em;
  }
  .brand {
    top: 482px;
    display: flex;
    align-items: center;
    gap: 12px;
  }
  .brand__mark {
    width: 46px;
    height: 46px;
    border: 1.5px solid var(--teal);
    border-radius: 50%;
  }
  .brand__name {
    font-size: 14px;
    font-weight: 400;
    letter-spacing: 0.3em;
    line-height: 1.25;
    color: var(--teal);
  }
  .host-photo {
    position: absolute;
    left: 308px;
    top: 9px;
    width: 245px;
    height: 544px;
    border-radius: 60px 60px 0 0;
    background: linear-gradient(180deg, #4a4a4e 0%, #2f3033 55%, #2e3a55 100%);
  }
</style>
</head>
<body>
<main class="stage">

  <section class="cover cover--logo" aria-label="Podcast cover, logo version">
    <div class="cover__top-band"></div>
    <div class="cover__line title-accent title-accent--one">TRUE</div>
    <div class="cover__line title-accent title-accent--two">PATH</div>
    <div class="cover__line title-main title-main--one">SLIM</div>
    <div class="cover__line title-main title-main--two">DOWN</div>
    <div class="cover__line label-podcast">PODCAST</div>
    <div class="cover__line label-with">with</div>
    <div class="cover__line host-name">DANE WARD</div>
    <div class="cover__line brand">
      <span class="brand__mark"></span>
      <span class="brand__name">MOVE BRIGHT<br>TRIM DOWN</span>
    </div>
  </section>

  <section class="cover cover--host" aria-label="Podcast cover, host photo version">
    <div class="cover__top-band"></div>
    <div class="host-photo" role="img" aria-label="Photo of the host standing, wearing a dark hoodie and jeans"></div>
    <div class="cover__line title-accent title-accent--one">TRUE</div>
    <div class="cover__line title-accent title-accent--two">PATH</div>
    <div class="cover__line title-main title-main--one">SLIM</div>
    <div class="cover__line title-main title-main--two">DOWN</div>
    <div class="cover__line label-podcast">PODCAST</div>
    <div class="cover__line label-with">with</div>
    <div class="cover__line host-name">DANE WARD</div>
    <div class="cover__line brand">
      <span class="brand__mark"></span>
      <span class="brand__name">MOVE BRIGHT<br>TRIM DOWN</span>
    </div>
  </section>

</main>
</body>
</html>
```